Stationary design for construction company

Want professional stationary and in the future brochures to use for contacting potential customers and existing customers. We are open to suggestions with existing logo. We are a contractor in the construction field that specializes in foundation plastering. We currently do other work but are looking to market and become the only go-to subcontractor for this specialty. I like the red and black contrast and the font which is "biner d". We want to present ourselves as a professional company so potential customers take us seriously.
Dunmore Stucco
86 N. Maple #415
Orem, Utah 84093
801.574.2281 Office
801.846.5037 Mobile
marla@dunmorestucco-example.com
neil@dunmorestucco-example.com
We will need to be able to edit the finished work incase future numbers, addresses and such change.
Thx
Marla
Target Market(s)
New and exiting customers in the building industry
Industry/Entity Type
Construction Company
Font styles to use
Other font styles liked:
- Biner D
Look and feel
Each slider illustrates characteristics of the customer's brand and the style your logo design should communicate.

```html
<!DOCTYPE html>
<html lang="en">
<head>
<meta charset="utf-8">
<title>Dunmore Stucco – Stationery</title>
<link href="https://fonts.googleapis.com/css2?family=Lato:wght@400;700;900&display=swap" rel="stylesheet">
<style>
  :root {
    --brand-red: #c80000;
    --flap-text: #e0504a;
    --ink: #111111;
    --body-text: #555555;
    --paper: #ffffff;
    --faint: #f0f0f0;
    --stitch: #4a1010;
    --bg-top: #6a6a6a;
    --bg-mid: #626262;
    --bg-bottom: #2a2a2a;
  }
  * { margin: 0; padding: 0; box-sizing: border-box; }
  html, body { width: 1039px; height: 1200px; overflow: hidden; }
  body {
    position: relative;
    font-family: "Lato", Arial, sans-serif;
    background: linear-gradient(to bottom, var(--bg-top) 0%, var(--bg-mid) 70%, var(--bg-bottom) 100%);
  }

  /* Brand name block */
  .brand { display: flex; align-items: center; gap: 5px; }
  .brand-square { background: var(--brand-red); flex: none; }
  .brand-name {
    font-weight: 900; color: var(--ink); text-transform: uppercase;
    line-height: 1.02; letter-spacing: 0.5px;
  }

  /* Cover folder */
  .cover {
    position: absolute; left: 94px; top: 121px; width: 392px; height: 587px;
    background: var(--brand-red); overflow: hidden;
  }
  .cover-stitch {
    position: absolute; left: 22px; top: 0; width: 4px; height: 100%;
    background: repeating-linear-gradient(to bottom, var(--stitch) 0 5px, #2a0606 5px 7px);
  }
  .cover-rule { position: absolute; left: 0; width: 100%; height: 1px; background: rgba(255,255,255,0.45); }
  .cover-rule.top { top: 69px; }
  .cover-rule.bottom { top: 545px; }
  .cover .brand { position: absolute; left: 114px; top: 10px; }
  .cover .brand-square { width: 34px; height: 50px; background: var(--paper); }
  .cover .brand-name { color: var(--paper); font-size: 21px; }

  /* Letterhead */
  .letterhead {
    position: absolute; left: 542px; top: 121px; width: 392px; height: 588px;
    background: var(--paper); overflow: hidden;
  }
  .letterhead-header {
    position: absolute; left: 0; top: 0; width: 100%; height: 52px;
    border-bottom: 1.5px solid var(--brand-red);
  }
  .letterhead .brand { position: absolute; left: 32px; top: 5px; }
  .letterhead .brand-square { width: 26px; height: 40px; }
  .letterhead .brand-name { font-size: 16px; }
  .header-phones {
    position: absolute; right: 27px; top: 20px; font-size: 5.5px; font-weight: 700;
    color: var(--ink); text-align: right; line-height: 12px;
  }
  .header-phones svg, .footer-contacts svg { vertical-align: middle; margin-left: 3px; }
  .recipient {
    position: absolute; left: 32px; top: 77px; font-size: 8px; color: #444; line-height: 13.7px;
  }
  .recipient .name { font-weight: 700; }
  .salutation { position: absolute; left: 32px; top: 167px; font-size: 9px; font-weight: 700; color: #444; }
  .letter-body { position: absolute; left: 31px; top: 187px; width: 332px; }
  .letter-body p {
    font-size: 5.4px; color: var(--body-text); line-height: 15px; text-align: justify;
    margin-bottom: 7px;
  }
  .signoff { position: absolute; left: 31px; top: 446px; font-size: 8px; color: #444; line-height: 15px; }
  .signoff .gap { display: block; height: 4px; }
  .closing { position: absolute; right: 34px; top: 446px; font-size: 8px; color: #444; }
  .letter-curve { position: absolute; left: 0; top: 0; }
  .footer-contacts {
    position: absolute; right: 10px; top: 548px; font-size: 5.5px; color: var(--paper);
    text-align: right; line-height: 8.8px;
  }

  /* Business card */
  .card {
    position: absolute; left: 50px; top: 779px; width: 453px; height: 226px;
    background: var(--paper);
  }
  .card .brand { position: absolute; left: 142px; top: 33px; gap: 7px; }
  .card .brand-square { width: 40px; height: 60px; }
  .card .brand-name { font-size: 25px; }
  .card-rule { position: absolute; left: 0; top: 196px; width: 100%; height: 1.5px; background: var(--brand-red); }
  .card-emails {
    position: absolute; left: 27px; top: 202px; font-size: 6.4px; color: #333; line-height: 9.6px;
  }
  .card-emails svg { vertical-align: middle; margin-right: 4px; }
  .card-phones {
    position: absolute; right: 23px; top: 202px; font-size: 6.4px; color: #333; line-height: 9.6px; text-align: right;
  }
  .card-phones .label { color: var(--brand-red); }

  /* Envelope */
  .envelope {
    position: absolute; left: 530px; top: 776px; width: 462px; height: 231px;
    background: var(--paper); overflow: hidden;
  }
  .envelope-flap { position: absolute; left: 0; top: 0; }
  .flap-name {
    position: absolute; left: 0; top: 7px; width: 100%; text-align: center;
    font-weight: 900; font-size: 17px; line-height: 1.1; color: var(--flap-text);
    text-transform: uppercase; letter-spacing: 0.5px;
  }
  .envelope-mark {
    position: absolute; left: 182px; top: 100px; width: 90px; height: 90px; background: var(--faint);
  }
</style>
</head>
<body>

  <section class="cover" aria-label="Presentation folder cover">
    <div class="cover-stitch"></div>
    <div class="cover-rule top"></div>
    <div class="cover-rule bottom"></div>
    <div class="brand">
      <span class="brand-square"></span>
      <span class="brand-name">Dunmore<br>Stucco</span>
    </div>
  </section>

  <section class="letterhead" aria-label="Letterhead">
    <svg class="letter-curve" width="392" height="588" viewBox="0 0 392 588" aria-hidden="true">
      <path d="M217 588 C300 545 370 470 392 388 L392 588 Z" fill="#c80000"/>
    </svg>
    <header class="letterhead-header">
      <div class="brand">
        <span class="brand-square"></span>
        <span class="brand-name">Dunmore<br>Stucco</span>
      </div>
      <div class="header-phones">
        801.574.2281<svg width="5" height="6" viewBox="0 0 10 12"><path d="M3 0 L5 3 L3.5 4.5 C4 7 5 8.5 7 9.5 L8.5 8 L10 10.5 L8 12 C3 10 0 6 1 1 Z" fill="#c80000"/></svg><br>
        801.846.5037<svg width="5" height="6" viewBox="0 0 10 12"><path d="M3 0 L5 3 L3.5 4.5 C4 7 5 8.5 7 9.5 L8.5 8 L10 10.5 L8 12 C3 10 0 6 1 1 Z" fill="#c80000"/></svg>
      </div>
    </header>

    <address class="recipient" style="font-style:normal">
      <span class="name">Daniel Hartley</span><br>
      Owner<br>
      Company Name<br>
      Address Line1, Address Line2<br>
      Country -123456
    </address>

    <p class="salutation">Dear Daniel Hartley</p>

    <div class="letter-body">
      <p>Lorem ipsum dolor sit amet, consectetur adipiscing elit, sed do eiusmod tempor incididunt ut labore et dolore magna aliqua. Ut enim ad minim veniam, quis nostrud exercitation ullamco laboris nisi ut aliquip ex ea commodo consequat. Duis aute irure dolor in reprehenderit in voluptate velit esse cillum dolore eu fugiat nulla pariatur. Excepteur sint occaecat cupidatat non proident, sunt in culpa qui officia deserunt mollit anim id est laborum.</p>
      <p>Lorem ipsum dolor sit amet, consectetur adipiscing elit, sed do eiusmod tempor incididunt ut labore et dolore magna aliqua. Ut enim ad minim veniam, quis nostrud exercitation ullamco laboris nisi ut aliquip ex ea commodo consequat. Duis aute irure dolor in reprehenderit in voluptate velit esse cillum dolore</p>
      <p>Lorem ipsum dolor sit amet, consectetur adipiscing elit, sed do eiusmod tempor incididunt ut labore et dolore magna aliqua. Ut enim ad minim veniam, quis nostrud exercitation ullamco laboris nisi ut aliquip ex ea commodo consequat. Duis aute irure dolor in reprehenderit in voluptate velit esse cillum dolore eu fugiat nulla pariatur. Excepteur sint occaecat cupidatat non proident, sunt in culpa qui officia deserunt mollit anim id est laborum.</p>
    </div>

    <div class="signoff">
      Sincerely,<span class="gap"></span>
      [ your Name ]<br>
      [ Title ]
    </div>
    <div class="closing">Your Faithfully</div>

    <div class="footer-contacts">
      marla@dunmorestucco-example.com<svg width="5" height="4" viewBox="0 0 10 8"><rect width="10" height="8" fill="#fff"/><path d="M0 0 L5 4 L10 0" stroke="#c80000" fill="none"/></svg><br>
      neil@dunmorestucco-example.com<svg width="5" height="4" viewBox="0 0 10 8"><rect width="10" height="8" fill="#fff"/><path d="M0 0 L5 4 L10 0" stroke="#c80000" fill="none"/></svg><br>
      86 N. Maple #415 Orem, Utah 84093<svg width="4" height="6" viewBox="0 0 8 12"><path d="M4 0 C1.5 0 0 2 0 4 C0 7 4 12 4 12 C4 12 8 7 8 4 C8 2 6.5 0 4 0 Z" fill="#fff"/><circle cx="4" cy="4" r="1.5" fill="#c80000"/></svg>
    </div>
  </section>

  <section class="card" aria-label="Business card">
    <div class="brand">
      <span class="brand-square"></span>
      <span class="brand-name">Dunmore<br>Stucco</span>
    </div>
    <div class="card-rule"></div>
    <div class="card-emails">
      <svg width="6" height="5" viewBox="0 0 10 8"><rect width="10" height="8" fill="#c80000"/><path d="M0 0 L5 4 L10 0" stroke="#fff" fill="none"/></svg>marla@dunmorestucco-example.com<br>
      <svg width="6" height="5" viewBox="0 0 10 8"><rect width="10" height="8" fill="#c80000"/><path d="M0 0 L5 4 L10 0" stroke="#fff" fill="none"/></svg>neil@dunmorestucco-example.com
    </div>
    <div class="card-phones">
      801.574.2281 - <span class="label">Office</span><br>
      801.846.5037 - <span class="label">Mobile</span>
    </div>
  </section>

  <section class="envelope" aria-label="Envelope">
    <svg class="envelope-flap" width="462" height="52" viewBox="0 0 462 52" aria-hidden="true">
      <polygon points="0,0 462,0 445,51 17,51" fill="#c80000"/>
    </svg>
    <div class="flap-name">Dunmore<br>Stucco</div>
    <div class="envelope-mark"></div>
  </section>

</body>
</html>
```